Portal Panel Medic need professional looking business card printed on plastic, Commericial, Industri

We are family owned and operated garage door company in Indianapolis, Indiana. We sale service and install dock equipment, doors, operators. We are looking to expand our commercial/ industrial division. We also service all residential doors and operators. We are looking for a business that stands out of the crowd. We are committed to have the best customer service in the industry.

Target Market(s)

National and local general contractors, National/ Corpate service accounts,

Industry/Entity Type

Business Service

Contact Information for Business Card

To be printed on plastic stock

Font styles to use
Sans Serif

Colors
ffffff
f04a50
ec1f27

Requirements
Must have
• Name, website,email, phone number, position.
Nice to have
• A standout professional design

```html
<!DOCTYPE html>
<html lang="en">
<head>
<meta charset="utf-8">
<title>Portal Panel Medic – Business Card</title>
<link rel="stylesheet" href="https://fonts.googleapis.com/css2?family=Open+Sans:wght@400;600;800&display=swap">
<style>
  :root {
    --red: #ec1f27;
    --red-soft: #f04a50;
    --red-deep: #c41e24;
    --white: #ffffff;
    --paper: #f1f1f1;
    --ink: #1c1c1c;
    --muted: #3a3a3a;
    --bg: #ffffff;
  }
  * { margin: 0; padding: 0; box-sizing: border-box; }
  html, body {
    width: 1200px; height: 1200px; overflow: hidden;
    background: var(--bg);
    font-family: "Open Sans", sans-serif;
  }
  .canvas { position: relative; width: 1200px; height: 1200px; }

  .card { position: absolute; left: 190px; width: 840px; height: 480px; }
  .card--front {
    top: 46px;
    background: linear-gradient(160deg, var(--red-deep) 0%, var(--red) 45%, var(--red-soft) 100%);
  }
  .card--back {
    top: 646px;
    background: linear-gradient(180deg, #ececec 0%, var(--paper) 50%, #ededed 100%);
  }

  .mascot {
    position: absolute; border-radius: 40px 40px 12px 12px;
    background: linear-gradient(180deg, #e6e6e6 0%, #bdbdbd 55%, #5a3a2a 100%);
  }
  .card--front .mascot { left: 192px; top: 166px; width: 98px; height: 212px; }
  .card--back .mascot { left: 96px; top: 202px; width: 74px; height: 162px; }

  .wordmark {
    position: absolute; white-space: nowrap;
    font-weight: 800; line-height: 1;
  }
  .card--front .wordmark { left: 306px; top: 254px; font-size: 36px; color: var(--white); }
  .card--back .wordmark { left: 182px; top: 268px; font-size: 25px; color: var(--red); }

  .side-band { position: absolute; top: 172px; width: 40px; height: 166px; }
  .side-band--left { left: 0; background: var(--red-deep); }
  .side-band--right { right: 0; background: var(--red); }

  .contact {
    position: absolute; left: 514px; top: 170px; list-style: none;
    color: var(--ink); font-size: 12.5px;
  }
  .contact__row { position: relative; padding-left: 30px; line-height: 16px; }
  .contact__icon { position: absolute; left: 0; top: 0; width: 18px; height: 18px; }
  .contact__row--person { margin-bottom: 20px; }
  .contact__name { color: var(--red); font-weight: 600; font-size: 15px; line-height: 18px; }
  .contact__title { color: var(--muted); font-size: 12px; margin-top: 4px; }
  .contact__row--phone { margin-bottom: 12px; }
  .contact__row--web { margin-bottom: 8px; }
  .contact__row--address { margin-bottom: 10px; }
</style>
</head>
<body>
<div class="canvas">

  <section class="card card--front">
    <div class="mascot" role="img" aria-label="Illustrated mascot of a repair technician in a white coat with a stethoscope"></div>
    <div class="wordmark">Portal Panel Medic</div>
  </section>

  <section class="card card--back">
    <div class="side-band side-band--left"></div>
    <div class="side-band side-band--right"></div>

    <div class="mascot" role="img" aria-label="Illustrated mascot of a repair technician in a white coat with a stethoscope"></div>
    <div class="wordmark">Portal Panel Medic</div>

    <ul class="contact">
      <li class="contact__row contact__row--person">
        <svg class="contact__icon" viewBox="0 0 18 18"><rect width="18" height="18" rx="3" fill="#f04a50"/><circle cx="9" cy="6.5" r="2.6" fill="#fff"/><path d="M4 14c0-3 2.2-4.5 5-4.5s5 1.5 5 4.5z" fill="#fff"/></svg>
        <div class="contact__name">Dale Mercer</div>
        <div class="contact__title">Graphic Designer</div>
      </li>
      <li class="contact__row contact__row--phone">
        <svg class="contact__icon" viewBox="0 0 18 18"><rect width="18" height="18" rx="3" fill="#f04a50"/><path d="M4 7.5c0-2 2.2-3 5-3s5 1 5 3v1h-2.5V7H6.5v1.5H4z" fill="#fff"/><rect x="5.5" y="9.5" width="7" height="4" rx="1" fill="#fff"/></svg>
        (555) 204-7731
      </li>
      <li class="contact__row contact__row--web">
        <svg class="contact__icon" viewBox="0 0 18 18"><rect width="18" height="18" rx="3" fill="#f04a50"/><circle cx="9" cy="9" r="5" fill="none" stroke="#fff" stroke-width="1.4"/><path d="M4 9h10M9 4c2 2.5 2 7.5 0 10M9 4c-2 2.5-2 7.5 0 10" fill="none" stroke="#fff" stroke-width="1"/></svg>
        www.portalpanelmedic.com
      </li>
      <li class="contact__row contact__row--address">
        <svg class="contact__icon" viewBox="0 0 18 18"><rect width="18" height="18" rx="3" fill="#f04a50"/><path d="M9 3.5a3.8 3.8 0 0 1 3.8 3.8C12.8 10 9 14.5 9 14.5S5.2 10 5.2 7.3A3.8 3.8 0 0 1 9 3.5z" fill="#fff"/><circle cx="9" cy="7.3" r="1.4" fill="#f04a50"/></svg>
        4280 E Marlow Ave Ste C<br>Brookhaven, OH 44102
      </li>
      <li class="contact__row contact__row--email">
        <svg class="contact__icon" viewBox="0 0 18 18"><rect width="18" height="18" rx="3" fill="#f04a50"/><rect x="3.5" y="5" width="11" height="8" fill="#fff"/><path d="M3.5 5l5.5 4.5L14.5 5" fill="none" stroke="#f04a50" stroke-width="1.2"/></svg>
        info@portalpanelmedic.com
      </li>
    </ul>
  </section>

</div>
</body>
</html>
```